R&T Promotions / P.L.W. Sales Business Cards

I have 2 companies that are somewhat connected, yet sell to 2 different markets.

R&T Promotions www.rotapfx.example

We are a manufacturers representative company. We handle sales and marketing of Home Theater, Home Automation, Audio & Video products for the state of Florida. We work with Designers, Architects, Technology Consultants and Electronic Integrators to design, sell and install cutting edge technology in new and existing homes, condos and commercial spaces.

P.L.W. Sales www.plwqz.example

We are a manufacturers representative company. We handle sales and marketing of automotive Audio, Electronics, Security, Navigation and Entertainment products for the state of Florida. We work with 12-volt retailers, installers and automobile customizers to design, sell, merchandise, fabricate and install cutting edge technology in cars, boats, motor coaches, etc.

We have logo's that might still be relevant, but might need a little touching up. We need a new business card design and layout for each of the 2 companies. I would like them to have a family look, but still better speak to the customer base associated with the channel.

Target Market(s)

R&T Promotions -

Design, Engineering, Construction, Technology, elegant, tasteful.

P.L.W. Sales -

More cutting edge, industrial, youth, aggressive, fun, bold.

Industry/Entity Type

Business

Requirements
Must have
• New business card layout for both companies.
Nice to have
• A family look, or relationship to the other company. Even if it's just a logo referencing the other company.

```html
<!DOCTYPE html>
<html lang="en">
<head>
<meta charset="utf-8">
<title>R&amp;T Promotions / P.L.W. Sales Business Cards</title>
<link href="https://fonts.googleapis.com/css2?family=Russo+One&family=Lato:wght@300;400&display=swap" rel="stylesheet">
<style>
  :root {
    --backdrop: #ecebe8;
    --ink-black: #141414;
    --ink-white: #ffffff;
    --card-light: #d9d6d2;
    --text-grey: #4a4a4a;
    --rule-grey: #5a5a5a;
  }
  * { margin: 0; padding: 0; box-sizing: border-box; }
  html, body { width: 1200px; height: 900px; overflow: hidden; }
  body { background: var(--backdrop); position: relative; }

  .card {
    position: absolute;
    width: 560px;
    height: 320px;
    overflow: hidden;
    box-shadow: 0 6px 18px rgba(0,0,0,0.18);
  }

  /* P.L.W. Sales card */
  .card--plw {
    left: 80px; top: 90px;
    background: var(--ink-black);
    color: var(--ink-white);
    font-family: "Russo One", sans-serif;
  }
  .plw-badge {
    position: absolute;
    right: -10px; top: -40px;
    width: 170px; height: 170px;
    border-radius: 50%;
    background: var(--ink-white);
    display: flex; align-items: center; justify-content: center;
    padding-top: 40px;
  }
  .plw-badge__name {
    color: var(--ink-black);
    font-size: 22px;
    line-height: 1.05;
    text-align: center;
    margin-right: 10px;
  }
  .plw-identity {
    position: absolute;
    left: 120px; top: 38px;
    width: 220px;
    text-align: center;
    font-size: 17px;
    line-height: 1.2;
    letter-spacing: 0.5px;
  }
  .plw-rule {
    position: absolute;
    left: 40px; top: 96px;
    width: 345px; height: 4px;
    background: var(--ink-white);
  }
  .plw-rule--short {
    left: 40px; top: 150px;
    width: 210px; height: 3px;
  }
  .plw-contact {
    position: absolute;
    left: 40px; top: 158px;
    font-size: 15px;
    line-height: 20px;
    list-style: none;
    letter-spacing: 0.4px;
  }
  .plw-stripes { position: absolute; right: 0; bottom: 0; }

  /* R&T Promotions card */
  .card--rt {
    left: 560px; top: 490px;
    background: linear-gradient(135deg, #e0ddd9 0%, var(--card-light) 60%, #cfccc8 100%);
    color: var(--text-grey);
    font-family: "Lato", sans-serif;
    font-weight: 300;
  }
  .rt-wordmark {
    position: absolute;
    right: 34px; top: 26px;
    display: flex; align-items: center; gap: 8px;
    font-size: 22px;
    font-weight: 400;
    color: var(--ink-black);
  }
  .rt-wordmark__dot {
    width: 14px; height: 14px;
    background: var(--ink-black);
  }
  .rt-identity {
    position: absolute;
    left: 36px; top: 54px;
    font-size: 25px;
    line-height: 1.2;
  }
  .rt-details {
    position: absolute;
    left: 180px; top: 118px;
    list-style: none;
    font-size: 16.5px;
    line-height: 22px;
  }
  .rt-details__row { display: flex; }
  .rt-details__label {
    width: 112px;
    padding-right: 10px;
    text-align: right;
    flex: none;
  }
  .rt-details__value {
    position: relative;
    padding-left: 12px;
    border-left: 1px solid var(--rule-grey);
    white-space: nowrap;
  }
  .rt-details__row--labelled .rt-details__value::before {
    content: "";
    position: absolute;
    left: -6px; top: 11px;
    width: 11px; height: 1px;
    background: var(--rule-grey);
  }
</style>
</head>
<body>

  <section class="card card--plw" aria-label="P.L.W. Sales business card">
    <div class="plw-badge"><span class="plw-badge__name">P.L.W.<br>SALES</span></div>
    <div class="plw-identity">
      <p>DALE ORMSBY</p>
      <p>- REP PRINCIPLE -</p>
    </div>
    <div class="plw-rule"></div>
    <div class="plw-rule plw-rule--short"></div>
    <ul class="plw-contact">
      <li>TEL: 800-555-0147</li>
      <li>FAX: 305-555-0193</li>
      <li>dale@plw-rt.example</li>
      <li>HTTP://WWW.PLW-RT.EXAMPLE</li>
      <li>4120 NW 88TH STREET</li>
      <li>DORAL, FL 33178</li>
    </ul>
    <svg class="plw-stripes" width="220" height="200" viewBox="0 0 220 200" aria-hidden="true">
      <polygon points="220,20 220,52 92,200 58,200" fill="var(--ink-white)"/>
      <polygon points="220,80 220,100 142,200 118,200" fill="var(--ink-white)"/>
    </svg>
  </section>

  <section class="card card--rt" aria-label="R&amp;T Promotions business card">
    <div class="rt-wordmark"><span class="rt-wordmark__dot"></span>R&amp;T Promotions</div>
    <div class="rt-identity">
      <p>Nolan Varick</p>
      <p>- Rep Principle -</p>
    </div>
    <ul class="rt-details">
      <li class="rt-details__row rt-details__row--labelled"><span class="rt-details__label">Address</span><span class="rt-details__value">4120 NW 88th Street</span></li>
      <li class="rt-details__row"><span class="rt-details__label"></span><span class="rt-details__value">Doral, FL 33178</span></li>
      <li class="rt-details__row rt-details__row--labelled"><span class="rt-details__label">Telephone</span><span class="rt-details__value">800-555-0147</span></li>
      <li class="rt-details__row rt-details__row--labelled"><span class="rt-details__label">Cell</span><span class="rt-details__value">727-555-0162</span></li>
      <li class="rt-details__row rt-details__row--labelled"><span class="rt-details__label">Fax</span><span class="rt-details__value">305-555-0193</span></li>
      <li class="rt-details__row rt-details__row--labelled"><span class="rt-details__label">EMail</span><span class="rt-details__value">nolan@plw-rt.example</span></li>
      <li class="rt-details__row rt-details__row--labelled"><span class="rt-details__label">Website</span><span class="rt-details__value">www.plw-rt.example</span></li>
    </ul>
  </section>

</body>
</html>
```